Business Card Design

Our Motto is "Protecting Australia's Underground Utilities"

We want the Southern Cross inside a shield I have attached the southern cross and our old shield design

Product description is: Vacuum Excavation & Utility Location
Wet & Dry Vacuum Loading
Confined Space Entry Specialists
High Pressure Cleaning

The Southern Cross in the shield must be blue and white. The Company name must be Coastal Pipeline Guard. The Green & Gold Shield logo I uploaded is my OLD logo design. Thank you

Target Market(s)

Civil Construction

Industry/Entity Type

Business

Contact Information for Business Card

Coastal Pipeline Guard Pty Ltd
Corey Hallworth(Director)
0413862051
coreyh@pipeguardco.com.au
A.B.N.52938407716

Colors
0456a3

Requirements
Must have
• Southern Cross inside a shield, Blue and white design on the Southern Cross shield.
Must say Coastal Pipeline Guard P/L

```html
<!DOCTYPE html>
<html lang="en">
<head>
<meta charset="utf-8">
<title>Coastal Pipeline Guard – Business Card</title>
<link rel="stylesheet" href="https://fonts.googleapis.com/css2?family=Roboto+Condensed:wght@700&family=Open+Sans:wght@400;600&display=swap">
<style>
  :root {
    --brand-blue: #0456a3;
    --deep-blue: #1d3f98;
    --navy: #16307f;
    --pale-blue: #c9d5ec;
    --card-white: #ffffff;
    --backdrop: #eceef2;
    --ink-blue: #1c3d96;
  }
  html, body {
    margin: 0;
    width: 1200px;
    height: 784px;
    overflow: hidden;
    background: var(--backdrop);
  }
  .card {
    position: absolute;
    width: 540px;
    height: 316px;
    overflow: hidden;
    box-shadow: 0 6px 18px rgba(20, 40, 90, 0.18);
  }
  /* Services side */
  .card-back {
    left: 40px;
    top: 234px;
    background: linear-gradient(135deg, var(--brand-blue) 0%, var(--deep-blue) 55%, var(--navy) 100%);
  }
  .service-list {
    list-style: none;
    margin: 0;
    padding: 0;
    position: absolute;
    left: 28px;
    top: 36px;
  }
  .service-list li {
    display: flex;
    align-items: center;
    gap: 9px;
    height: 34px;
    font-family: "Roboto Condensed", sans-serif;
    font-weight: 700;
    font-size: 15px;
    letter-spacing: 0.6px;
    text-transform: uppercase;
    color: var(--card-white);
  }
  .star-bullet { width: 18px; height: 18px; fill: var(--card-white); }
  .brand {
    position: absolute;
    width: 170px;
    text-align: center;
    font-family: "Roboto Condensed", sans-serif;
    font-weight: 700;
    font-size: 19px;
    line-height: 1.15;
    letter-spacing: 1px;
    text-transform: uppercase;
  }
  .brand .brand-dot {
    display: block;
    width: 70px;
    height: 70px;
    margin: 0 auto 10px;
    border-radius: 50%;
  }
  .brand-back { right: 34px; top: 96px; color: var(--card-white); }
  .brand-back .brand-dot { background: var(--card-white); }
  /* Contact side */
  .card-front {
    left: 620px;
    top: 234px;
    background: var(--card-white);
  }
  .sweep { position: absolute; inset: 0; width: 540px; height: 316px; }
  .brand-front { left: 50px; top: 30px; color: var(--ink-blue); }
  .brand-front .brand-dot { background: var(--brand-blue); }
  .contact {
    position: absolute;
    left: 330px;
    top: 150px;
    font-family: "Open Sans", sans-serif;
    color: var(--card-white);
  }
  .contact-name { font-size: 17px; font-weight: 400; margin: 0; line-height: 1.2; }
  .contact-role { font-size: 11px; margin: 2px 0 12px; }
  .contact-line {
    display: flex;
    align-items: center;
    gap: 6px;
    font-size: 13px;
    line-height: 1.35;
  }
  .contact-line.email { font-size: 12px; }
  .contact-icon { width: 12px; height: 12px; fill: var(--card-white); }
  .contact-abn { font-size: 11px; padding-left: 18px; line-height: 1.4; }
</style>
</head>
<body>

<section class="card card-back" aria-label="Services side">
  <ul class="service-list">
    <li><svg class="star-bullet" viewBox="0 0 24 24"><path d="M12 1.5l3.1 6.9 7.4.7-5.6 5 1.7 7.4L12 17.6l-6.6 3.9 1.7-7.4-5.6-5 7.4-.7z"/></svg>Vacuum Excavation &amp; Utility Location</li>
    <li><svg class="star-bullet" viewBox="0 0 24 24"><path d="M12 1.5l3.1 6.9 7.4.7-5.6 5 1.7 7.4L12 17.6l-6.6 3.9 1.7-7.4-5.6-5 7.4-.7z"/></svg>Wet &amp; Dry Vacuum Loading</li>
    <li><svg class="star-bullet" viewBox="0 0 24 24"><path d="M12 1.5l3.1 6.9 7.4.7-5.6 5 1.7 7.4L12 17.6l-6.6 3.9 1.7-7.4-5.6-5 7.4-.7z"/></svg>Confined Space Entry Specialists</li>
    <li><svg class="star-bullet" viewBox="0 0 24 24"><path d="M12 1.5l3.1 6.9 7.4.7-5.6 5 1.7 7.4L12 17.6l-6.6 3.9 1.7-7.4-5.6-5 7.4-.7z"/></svg>High Pressure Cleaning</li>
  </ul>
  <div class="brand brand-back"><span class="brand-dot"></span>Coastal<br>Pipeline Guard</div>
</section>

<section class="card card-front" aria-label="Contact side">
  <svg class="sweep" viewBox="0 0 540 316" aria-hidden="true">
    <defs>
      <linearGradient id="sweep-blue" x1="0" y1="1" x2="1" y2="0">
        <stop offset="0" stop-color="#16307f"/>
        <stop offset="0.6" stop-color="#1d3f98"/>
        <stop offset="1" stop-color="#0456a3"/>
      </linearGradient>
    </defs>
    <path d="M30 316 C130 190 290 100 540 6 L540 30 C300 120 160 200 60 316 Z" fill="var(--pale-blue)"/>
    <path d="M60 316 C160 200 300 120 540 30 L540 316 Z" fill="url(#sweep-blue)"/>
  </svg>

  <div class="brand brand-front"><span class="brand-dot"></span>Coastal<br>Pipeline Guard</div>

  <div class="contact">
    <p class="contact-name">Corey Hallworth</p>
    <p class="contact-role">Director</p>
    <div class="contact-line">
      <svg class="contact-icon" viewBox="0 0 24 24"><path d="M6.6 10.8a15.5 15.5 0 006.6 6.6l2.2-2.2a1 1 0 011-.25 11.4 11.4 0 003.6.57 1 1 0 011 1V20a1 1 0 01-1 1A17 17 0 013 4a1 1 0 011-1h3.5a1 1 0 011 1c0 1.25.2 2.45.57 3.57a1 1 0 01-.25 1z"/></svg>
      0413862051
    </div>
    <div class="contact-line email">
      <svg class="contact-icon" viewBox="0 0 24 24"><path d="M2 5h20v14H2z M2 5l10 8 10-8" fill="none" stroke="#fff" stroke-width="2.2"/></svg>
      coreyh@pipeguardco.com.au
    </div>
    <div class="contact-abn">A.B.N.52938407716</div>
  </div>
</section>

</body>
</html>
```